Coaching business needs flyer for business market

I need a flyer that I can send to HR-managers and business owners to inform them of my coaching services for organisations. We have three services: organisational- and teamcoaching, individual coaching and training programs.
I want the flyer to express calmness, solid and trustworthy coaching. As a person I am open and think out of the box.

In my logo I use a couple of colours (blue, green, orange and grey) that represent the diversity of humans. My company's name is Brookfield Alignment & Coaching and tag line is "Ignite your inner light".

I do not want the design to be too busy but also not too boring. I tried making something myself. Feel free to build on that design. Or feel free to start from scratch.

```html
<!DOCTYPE html>
<html lang="nl">
<head>
<meta charset="utf-8">
<title>Brookfield Alignment &amp; Coaching – flyer</title>
<link rel="stylesheet" href="https://fonts.googleapis.com/css2?family=Poppins:wght@400;500;700;800&family=Dancing+Script:wght@700&family=Kalam:wght@700&display=swap">
<style>
  :root{
    --backdrop:#a39a9b;
    --paper:#eef5f3;
    --panel:#bee4e0;
    --teal-dark:#1f6e6b;
    --teal-mid:#6fada7;
    --ink:#2f3436;
    --heading:#3b3d3f;
    --red:#d4432f;
    --red-deep:#c63a2a;
    --blue:#2379a9;
    --blue-deep:#1b6d9b;
    --orange:#f8a43c;
    --orange-deep:#f3931f;
    --script-blue:#1e5f8f;
    --grey:#5e6264;
    --white:#ffffff;
  }
  *{box-sizing:border-box;margin:0;padding:0}
  html,body{width:971px;height:1200px;overflow:hidden;background:var(--backdrop)}
  body{position:relative;font-family:"Poppins",sans-serif;color:var(--ink)}

  .flyer{position:absolute;left:106px;top:101px;width:768px;height:994px;
    background:linear-gradient(180deg,#f4f7f6 0%,var(--paper) 55%,#e4f1ee 100%);overflow:hidden}

  .intro{position:absolute;left:38px;top:42px;width:697px;height:240px;
    background:var(--panel);border-radius:22px;overflow:hidden}
  .portrait{position:absolute;left:0;top:8px;width:236px;height:232px;
    border-radius:110px 110px 0 0;
    background:radial-gradient(circle at 50% 45%,#c08a62 0%,#8e5f41 45%,#3a2c28 80%)}
  .coach-name{position:absolute;left:247px;top:22px;font-family:"Dancing Script",cursive;
    font-weight:700;font-size:38px;color:var(--teal-dark);line-height:1}
  .coach-bio{position:absolute;left:249px;top:73px;width:420px;font-size:11.3px;
    line-height:13.5px;color:var(--ink)}
  .quote-mark{position:absolute;left:552px;top:188px;font-family:Georgia,serif;
    font-size:140px;line-height:1;color:var(--teal-mid);font-weight:700}

  .service{position:absolute;top:391px;width:228px;border-radius:16px;color:var(--white);
    box-shadow:0 3px 8px rgba(0,0,0,.12)}
  .service--team{left:37px;height:351px;background:linear-gradient(160deg,var(--red) 0%,var(--red-deep) 100%)}
  .service--individual{left:274px;height:366px;background:linear-gradient(160deg,var(--blue) 0%,var(--blue-deep) 100%)}
  .service--training{left:512px;height:351px;background:linear-gradient(160deg,var(--orange) 0%,var(--orange-deep) 100%)}
  .service-photo{position:absolute;left:37px;top:-77px;width:154px;height:154px;border-radius:50%;
    border:3px solid var(--accent);box-shadow:inset 0 0 0 6px var(--white);background-clip:padding-box}
  .service--team .service-photo{--accent:var(--red);background:radial-gradient(circle,#d9b9a0 0%,#8f6a55 70%,#6e5144 100%)}
  .service--individual .service-photo{--accent:var(--blue);background:radial-gradient(circle,#e8e2da 0%,#b9aea3 70%,#8d8279 100%)}
  .service--training .service-photo{--accent:var(--orange);background:radial-gradient(circle,#5b6282 0%,#2b2d3c 70%,#17171f 100%)}
  .service-title{position:absolute;left:0;right:0;top:89px;text-align:center;font-weight:800;
    font-size:15px;line-height:18px;text-transform:uppercase}
  .service--team .service-title{color:#fbe3dc}
  .service--individual .service-title{color:#e6f2fa}
  .service--training .service-title{color:#fff6e8}
  .service-list{position:absolute;left:0;right:0;top:140px;list-style:none}
  .service-list li{position:relative;padding-left:58px;padding-right:8px;font-size:11px;line-height:13.5px;min-height:27px}
  .service--team li,.service--individual li{margin-bottom:14px}
  .service--training li{margin-bottom:16px;min-height:14px}
  .q-icon{position:absolute;left:31px;top:-1px;width:20px;height:20px;border-radius:50%;
    background:var(--white);border:2px solid rgba(255,255,255,.7);box-shadow:0 0 0 1.5px var(--white);
    font-weight:800;font-size:13px;line-height:17px;text-align:center}
  .service--team .q-icon{color:var(--red)}
  .service--individual .q-icon{color:var(--blue)}
  .service--training .q-icon{color:var(--orange-deep)}

  .results-heading{position:absolute;left:0;right:0;top:781px;text-align:center;font-weight:800;
    font-size:22.5px;letter-spacing:-.3px;color:var(--heading)}
  .results-script{position:absolute;left:0;right:0;top:808px;text-align:center;font-family:"Kalam",cursive;
    font-weight:700;font-size:36px;color:var(--script-blue);line-height:1.2}
  .methods{position:absolute;left:58px;top:861px;width:500px;list-style:none;font-size:12px;line-height:15.5px}
  .methods li{position:relative;padding-left:20px;margin-bottom:4px}
  .methods svg{position:absolute;left:0;top:1px}
  .brand{position:absolute;left:560px;top:836px;width:196px;text-align:center}
  .brand-dot{width:52px;height:52px;border-radius:50%;border:2px solid var(--grey);margin:0 auto 8px}
  .brand-name{font-weight:500;font-size:17px;line-height:21px;color:var(--grey)}
</style>
</head>
<body>
<main class="flyer">
  <section class="intro">
    <div class="portrait" role="img" aria-label="Portretfoto van de coach, lachend"></div>
    <h1 class="coach-name">Marisol Verhaven</h1>
    <p class="coach-bio">is trainer en coach. Ze heeft ruime ervaring met veranderingstrajecten binnen organisaties. Mensen omschrijven haar als ‘betrokken, warm, stevig en kordaat’. Het is haar passie om organisaties, teams en mensen te helpen groeien. Zij helpt weerstand te overwinnen en draagt bij aan groei in zelfvertrouwen. Haar trainingen en coaching zijn erop gericht om snel inzichtelijk te krijgen welke stappen men moet zetten om verder te komen. Ze gelooft de veranderkracht van de mensen waar ze mee werkt.<br>Ze is er om steun en richting te bieden en laat<br>hen zelf aan het roer.</p>
  </section>
  <div class="quote-mark" aria-hidden="true">”</div>

  <section class="service service--team">
    <div class="service-photo" role="img" aria-label="Foto van een teamcoachingsessie in een ruimte"></div>
    <h2 class="service-title">Organisational and<br>teamcoaching</h2>
    <ul class="service-list">
      <li><span class="q-icon">?</span>Heb je zorgen voor of na een fusie of verandering?</li>
      <li><span class="q-icon">?</span>Wil je missie, visie &amp; strategie ontwikkelen of wijzigen?</li>
      <li><span class="q-icon">?</span>Wens je de cultuur-veranderen of verder ontwikkelen?</li>
      <li><span class="q-icon">?</span>Beoog je de samenwerking bevorderen of verbeteren?</li>
    </ul>
  </section>

  <section class="service service--individual">
    <div class="service-photo" role="img" aria-label="Foto van een individuele coachingsessie"></div>
    <h2 class="service-title">Individual<br>coaching</h2>
    <ul class="service-list">
      <li><span class="q-icon">?</span>Wens je medewerkers die hun talent ten volste benutten?</li>
      <li><span class="q-icon">?</span>Verlang je meer authentieke leiderschap bij je collega’s?</li>
      <li><span class="q-icon">?</span>Wil je de mensen vooruit helpen in hun loopbaan?</li>
      <li><span class="q-icon">?</span>Zoek je steun voor medewerkers met burn-out of re-integratie?</li>
      <li><span class="q-icon">?</span>Heb je hulp nodig bij outplacement trajecten?</li>
    </ul>
  </section>

  <section class="service service--training">
    <div class="service-photo" role="img" aria-label="Foto van een trainingsgroep in een zaal"></div>
    <h2 class="service-title">Training<br>programs</h2>
    <ul class="service-list">
      <li><span class="q-icon">?</span>Leiderschap</li>
      <li><span class="q-icon">?</span>Communicatie</li>
      <li><span class="q-icon">?</span>Leren kijken met ‘systemische blik’ voor professionals</li>
      <li><span class="q-icon">?</span>Conflicthantering</li>
    </ul>
  </section>

  <h2 class="results-heading">Gedegen resultaat en kwaliteit door bewezen</h2>
  <p class="results-script">‘best practices’</p>
  <ul class="methods">
    <li><svg width="14" height="14" viewBox="0 0 14 14"><circle cx="6.5" cy="7.5" r="5.5" fill="none" stroke="#d4432f" stroke-width="1.5"/><path d="M3.5 7.5l2.5 2.5 7-8" fill="none" stroke="#d4432f" stroke-width="1.8"/></svg>Neuro Linguïstisch Programmeren (NLP)</li>
    <li><svg width="14" height="14" viewBox="0 0 14 14"><circle cx="6.5" cy="7.5" r="5.5" fill="none" stroke="#d4432f" stroke-width="1.5"/><path d="M3.5 7.5l2.5 2.5 7-8" fill="none" stroke="#d4432f" stroke-width="1.8"/></svg>Transactionele Analyse</li>
    <li><svg width="14" height="14" viewBox="0 0 14 14"><circle cx="6.5" cy="7.5" r="5.5" fill="none" stroke="#d4432f" stroke-width="1.5"/><path d="M3.5 7.5l2.5 2.5 7-8" fill="none" stroke="#d4432f" stroke-width="1.8"/></svg><strong>Systemisch Werken:</strong> Organisatieopstellingen, Familieopstellingen, Identity oriented Psycho Traumaopstellingen)</li>
    <li><svg width="14" height="14" viewBox="0 0 14 14"><circle cx="6.5" cy="7.5" r="5.5" fill="none" stroke="#d4432f" stroke-width="1.5"/><path d="M3.5 7.5l2.5 2.5 7-8" fill="none" stroke="#d4432f" stroke-width="1.8"/></svg>Somatic Experience, Ademwerk en Lichaamswerk</li>
  </ul>

  <div class="brand">
    <div class="brand-dot" aria-hidden="true"></div>
    <p class="brand-name">Brookfield Alignment<br>&amp; Coaching</p>
  </div>
</main>
</body>
</html>
```